Business Card Design for Tax Accounting Company

I need design files that can be edited to add new professional designations onto the end of my name once complete. I need design files that can be edited for new employees. I also need the design files to be able to upload into CardNest for new orders. I've attached multiple logo files with varying file extensions to help with the design.
Please include the following contact information:
Marcus Tellan, CFP®, EA, CTC, CEPA
Founder & CEO
C (480) 517.3082
F (623) 389.5170
718 W Larkspur Ave
Mesa, AZ 85210
Updates
I need the business card to include the following contact info:
C: (480)517.3082
F: (623) 389.5170
mt@RidgewayLedgerGroup.com
www.MarcusRTellan.com
Address to be included is
718 W Larkspur Ave
Mesa, AZ 85210
Business Cards are double sided
Target Market(s)
Business owners $1M+ annual revenue, especially for the construction and technology industries
Industry/Entity Type
Accounting & Tax
Contact Information for Business Card
Contact information and logo
Look and feel
Each slider illustrates characteristics of the customer's brand and the style your logo design should communicate.

```html
<!DOCTYPE html>
<html lang="en">
<head>
<meta charset="utf-8">
<title>Ridgeway Ledger Group – Business Cards</title>
<link rel="stylesheet" href="https://fonts.googleapis.com/css2?family=Noto+Serif:wght@400;700&display=swap">
<style>
  :root {
    --navy: #0d2466;
    --orange: #d25a1c;
    --white: #ffffff;
    --paper: #fbfbfa;
    --backdrop: #2b2c30;
  }
  * { box-sizing: border-box; margin: 0; padding: 0; }
  html, body { width: 1200px; height: 874px; overflow: hidden; }
  body {
    background: var(--backdrop);
    font-family: "Noto Serif", Georgia, serif;
    display: flex;
    flex-direction: column;
    align-items: center;
    justify-content: center;
    gap: 26px;
  }
  .card {
    width: 700px;
    height: 400px;
    border-radius: 22px;
    overflow: hidden;
    position: relative;
  }
  /* Back side */
  .card--back {
    background: var(--navy);
    color: var(--white);
    display: flex;
    flex-direction: column;
    align-items: center;
    justify-content: center;
    gap: 44px;
  }
  .back-brand {
    display: flex;
    align-items: center;
    gap: 16px;
    font-size: 40px;
    font-weight: 700;
    color: var(--white);
  }
  .back-brand .mark {
    width: 22px; height: 22px; border-radius: 50%;
    background: var(--orange);
  }
  .back-web {
    font-size: 15px;
    letter-spacing: 0.42em;
  }
  /* Front side */
  .card--front {
    background: var(--paper);
    display: flex;
    flex-direction: column;
  }
  .front-top {
    flex: 1;
    display: flex;
    flex-direction: column;
    align-items: center;
    justify-content: center;
    padding-top: 18px;
  }
  .brand-name {
    font-size: 34px;
    font-weight: 700;
    color: var(--navy);
    display: flex;
    align-items: center;
    gap: 12px;
  }
  .brand-name .mark {
    width: 16px; height: 16px; border-radius: 50%;
    background: var(--orange);
  }
  .tagline {
    margin-top: 8px;
    font-size: 12px;
    color: var(--navy);
  }
  .rule {
    height: 3px;
    background: var(--orange);
    border-bottom: 4px solid var(--paper);
    box-sizing: content-box;
  }
  .front-band {
    height: 168px;
    background: var(--navy);
    display: flex;
    align-items: center;
    justify-content: center;
    gap: 28px;
  }
  .person {
    text-align: right;
    color: var(--white);
    font-size: 15px;
    line-height: 1.3;
  }
  .person-name { color: var(--orange); font-size: 24px; font-weight: 700; line-height: 1.15; }
  .person-creds { color: var(--orange); font-size: 14px; margin-bottom: 4px; }
  .divider { width: 2px; height: 98px; background: var(--orange); }
  .contacts { list-style: none; color: var(--white); font-size: 15px; line-height: 1.45; }
  .contacts li { display: flex; align-items: center; gap: 10px; }
  .contacts svg { width: 13px; height: 13px; fill: var(--orange); flex: none; }
</style>
</head>
<body>
  <section class="card card--back">
    <div class="back-brand"><span class="mark"></span>Ridgeway Ledger Group</div>
    <div class="back-web">WWW.MARCUSRTELLAN.COM</div>
  </section>

  <section class="card card--front">
    <div class="front-top">
      <div class="brand-name"><span class="mark"></span>Ridgeway Ledger Group</div>
      <div class="tagline">Clear Numbers. Steady Guidance. Lasting Growth.</div>
    </div>
    <div class="rule"></div>
    <div class="front-band">
      <div class="person">
        <div class="person-name">Marcus Tellan</div>
        <div class="person-creds">CFP®, EA, CTC, CEPA</div>
        <div>718 W Larkspur Ave</div>
        <div>Mesa, AZ 85210</div>
      </div>
      <div class="divider"></div>
      <ul class="contacts">
        <li><svg viewBox="0 0 16 16" aria-hidden="true"><path d="M3 1l3 3-1.5 2c1 2 3 4 5 5L11.5 9.5l3 3-2 2.5C6 14 2 9 1 3z"/></svg>(480)517.3082</li>
        <li><svg viewBox="0 0 16 16" aria-hidden="true"><path d="M4 1h8v4H4zM1 6h14v7h-3v2H4v-2H1zM5 10v4h6v-4z"/></svg>(623) 389.5170</li>
        <li><svg viewBox="0 0 16 16" aria-hidden="true"><path d="M1 3h14v2L8 9 1 5zM1 7l7 4 7-4v6H1z"/></svg>mt@RidgewayLedgerGroup.com</li>
        <li><svg viewBox="0 0 16 16" aria-hidden="true"><circle cx="8" cy="8" r="7"/></svg>www.MarcusRTellan.com</li>
      </ul>
    </div>
  </section>
</body>
</html>
```